Bref créative
Calvane Chiropractic Stationary/Brochure/Business Card / Post-It Note Design
Calvane Chiropractic Motion and Vitality
Bright & Fun-filled
Marla Teversham, D.C., Diplomate Continental Spinal Council of Athletic Clinicians (w/ "registered' )
417 E Quarry Ln, Suite 83
PO Box 6289
Fernhollow OR 97302-0562
Dr.Marla@GoDrMarla.net
www.GoDrMarla.net
* clarification- title should have registered symbol on it
*I would like a Post It Note Design that has
Business Name, Tag Line, Phone Number and " A table is reserved for you and a line to write in appointment time.
* Please include tag line
*I've uploaded both a black background & white background version. I prefer the black background for its pop of color but realized that modifications for letterhead & brochures may be necessary.
the back of the card should have:
Certified Practitioner in the Following:
and then upload logos for
QEL
Pulsetap Systems
KQP / TBVX
VHP
GQLBR
Steelstride Provider

```html
<!DOCTYPE html>
<html lang="en">
<head>
<meta charset="utf-8">
<title>Calvane Chiropractic – Business Cards</title>
<link href="https://fonts.googleapis.com/css2?family=Cinzel:wght@400;600&family=Tinos:wght@400;700&display=swap" rel="stylesheet">
<style>
  :root{
    --stage:#1c1c1e;
    --green-light:#b6dc3a;
    --green:#86c21f;
    --green-dark:#3f7a0c;
    --purple:#7b2c9c;
    --purple-light:#a45ac4;
    --ink:#222;
    --paper:#ffffff;
    --night:#0b0b0b;
  }
  *{margin:0;padding:0;box-sizing:border-box}
  html,body{width:1200px;height:1004px;overflow:hidden;background:var(--stage)}
  .canvas{position:relative;width:1200px;height:1004px}
  .card{position:absolute;width:492px;height:295px;border-radius:12px;overflow:hidden;box-shadow:0 6px 18px rgba(0,0,0,.6)}
  .card svg.wave{position:absolute;inset:0;width:100%;height:100%}
  .front.light{background:var(--paper)}
  .front.dark{background:var(--night)}
  .brand{position:absolute;top:14px;left:0;right:0;text-align:center;font-family:"Cinzel",serif}
  .brand-mark{width:48px;height:48px;border-radius:50%;background:var(--purple);margin:0 auto 6px}
  .brand-name{color:var(--green);font-size:21px;font-weight:600;letter-spacing:.5px;line-height:1}
  .brand-sub{color:var(--purple);font-size:13px;font-weight:600;letter-spacing:1px;margin-top:2px}
  .brand-tag{color:var(--purple);font-size:8px;font-weight:600;letter-spacing:.3px;line-height:1.2;margin-top:2px}
  .dark .brand-sub,.dark .brand-tag{color:var(--purple-light)}
  .person{position:absolute;left:20px;top:196px;font-family:"Tinos",serif;color:var(--ink)}
  .person-name{font-size:19px;line-height:1.2}
  .person-title{font-size:13px;line-height:1.25}
  .contact{position:absolute;right:22px;top:160px;font-family:"Tinos",serif;font-size:10.5px;line-height:1.42;color:var(--ink);text-align:right;font-style:normal}
  .back{background:linear-gradient(160deg,var(--green-light),var(--green) 55%,var(--green-dark))}
  .back-deco{position:absolute;left:36px;top:60px;width:130px;height:130px;border-radius:50%;background:rgba(255,255,255,.14)}
  .back-title{position:absolute;left:50px;top:30px;font-family:"Cinzel",serif;font-size:13px;letter-spacing:1px;color:#fff}
  .badges{position:absolute;left:0;right:0;bottom:28px;height:58px;display:flex;align-items:center;justify-content:space-around;padding:0 12px}
  .back.light .badges{background:var(--paper)}
  .back.dark .badges{background:var(--night)}
  .badge{height:34px;border-radius:3px}
  .b1{width:40px;background:#c8202a}
  .b2{width:52px;background:#8a1f24}
  .b3{width:74px;background:#c21b1b}
  .b4{width:64px;background:#333}
  .b5{width:66px;background:#2d63a8}
  .b6{width:34px;height:40px;background:#555}
  .back.dark .b4,.back.dark .b6{background:#888}
</style>
</head>
<body>
<main class="canvas">

  <section class="card front light" style="left:90px;top:204px">
    <svg class="wave" viewBox="0 0 492 295" preserveAspectRatio="none" aria-hidden="true">
      <defs>
        <linearGradient id="gFront" x1="0" y1="0" x2="1" y2="1">
          <stop offset="0" stop-color="#c3e34a"/><stop offset=".6" stop-color="#8cc424"/><stop offset="1" stop-color="#4b8a10"/>
        </linearGradient>
      </defs>
      <path d="M0 170 C140 145 300 160 492 128 L492 295 L0 295Z" fill="url(#gFront)"/>
      <path d="M0 170 C140 145 300 160 492 128 L492 140 C300 172 140 160 0 182Z" fill="#7b2c9c"/>
    </svg>
    <div class="brand">
      <div class="brand-mark"></div>
      <div class="brand-name">CALVANE CHIROPRACTIC</div>
      <div class="brand-sub">MOTION AND VITALITY</div>
      <div class="brand-tag">MOVE FREELY, STAND TALL &amp; FEEL VIBRANT<br>IN EVERY SINGLE DAY!</div>
    </div>
    <div class="person">
      <div class="person-name">Marla Teversham, D.C.</div>
      <div class="person-title">Diplomate Continental Spinal Council<br>of Athletic Clinicians®</div>
    </div>
    <address class="contact">
      417 E Quarry Ln, Suite 83<br>PO Box 6289<br>Fernhollow OR 97302-0562<br>555-014-2290<br>555-018-3374<br>Dr.Marla@GoDrMarla.net<br>www.GoDrMarla.net
    </address>
  </section>

  <section class="card back light" style="left:608px;top:204px">
    <svg class="wave" viewBox="0 0 492 295" preserveAspectRatio="none" aria-hidden="true">
      <path d="M0 22 C150 4 330 34 492 8 L492 0 L0 0Z" fill="#fff"/>
      <path d="M0 22 C150 4 330 34 492 8 L492 18 C330 44 150 14 0 32Z" fill="#7b2c9c"/>
    </svg>
    <div class="back-deco" role="img" aria-label="Faint brand emblem decoration"></div>
    <div class="back-title">CERTIFIED PRACTITIONER IN THE FOLLOWING:</div>
    <div class="badges">
      <div class="badge b1"></div><div class="badge b2"></div><div class="badge b3"></div>
      <div class="badge b4"></div><div class="badge b5"></div><div class="badge b6"></div>
    </div>
  </section>

  <section class="card front dark" style="left:90px;top:517px">
    <svg class="wave" viewBox="0 0 492 295" preserveAspectRatio="none" aria-hidden="true">
      <defs>
        <linearGradient id="gFront2" x1="0" y1="0" x2="1" y2="1">
          <stop offset="0" stop-color="#c3e34a"/><stop offset=".6" stop-color="#8cc424"/><stop offset="1" stop-color="#4b8a10"/>
        </linearGradient>
      </defs>
      <path d="M0 170 C140 145 300 160 492 128 L492 295 L0 295Z" fill="url(#gFront2)"/>
      <path d="M0 170 C140 145 300 160 492 128 L492 140 C300 172 140 160 0 182Z" fill="#7b2c9c"/>
    </svg>
    <div class="brand">
      <div class="brand-mark"></div>
      <div class="brand-name">CALVANE CHIROPRACTIC</div>
      <div class="brand-sub">MOTION AND VITALITY</div>
      <div class="brand-tag">MOVE FREELY, STAND TALL &amp; FEEL VIBRANT<br>IN EVERY SINGLE DAY!</div>
    </div>
    <div class="person">
      <div class="person-name">Marla Teversham, D.C.</div>
      <div class="person-title">Diplomate Continental Spinal Council<br>of Athletic Clinicians®</div>
    </div>
    <address class="contact">
      417 E Quarry Ln, Suite 83<br>PO Box 6289<br>Fernhollow OR 97302-0562<br>555-014-2290<br>555-018-3374<br>Dr.Marla@GoDrMarla.net<br>www.GoDrMarla.net
    </address>
  </section>

  <section class="card back dark" style="left:608px;top:517px">
    <svg class="wave" viewBox="0 0 492 295" preserveAspectRatio="none" aria-hidden="true">
      <path d="M0 22 C150 4 330 34 492 8 L492 0 L0 0Z" fill="#0b0b0b"/>
      <path d="M0 22 C150 4 330 34 492 8 L492 18 C330 44 150 14 0 32Z" fill="#7b2c9c"/>
    </svg>
    <div class="back-deco" role="img" aria-label="Faint brand emblem decoration"></div>
    <div class="back-title">CERTIFIED PRACTITIONER IN THE FOLLOWING:</div>
    <div class="badges">
      <div class="badge b1"></div><div class="badge b2"></div><div class="badge b3"></div>
      <div class="badge b4"></div><div class="badge b5"></div><div class="badge b6"></div>
    </div>
  </section>

</main>
</body>
</html>
```